Re-design UI/UX for Online movie website

We need a stunning design for our online movie website www.vormalite.com

KALDORVUE is an online platform for the presentation of all visual art forms, particularly movies, feature films, short films, documentaries, game shows, reality shows, serials and traditional art forms of different languages for our international audience to indulge in.

We want a design & layout similar to leading online movie streaming websites such as Brimcast , Tavelo Crest , PLUMA BAY

Target Market(s)

Worldwide

Industry/Entity Type

Movie

Number of Pages Required

5+ page

Requirements
Must have
• Look & Feel - These are some of the suggestion. Please feel free to add as per industry standards. Be as creative as possible. The website needs to be really attractive. Movie listing , categories etc., should be easy to navigate
• 1 Text could be justified in all the pages
• 2 Font color may be changed to white color to be more visible.
• 3 Headings to be in Red color instead of Orange color. As Red will match the logo color as well
• 4 Heading to be consistent everywhere. Example in About us page " About us" font is capital, white in color and larger than the other 2 headings on the same page.
• 5 Chatterly, quibbr and Snapgrove links to be added
• 6 Menu options could be in white or red color to be more visible. Current grey color is looking dull.
• 8 One more menu tab to be included on the top named "Movies" or "Browse movies" . Under Browse Movies, add multilevel menu "New Releases" "Short Films" "Kaldorvue Originals" "Library" "All Movies" . Later categories like Comedy, Thriller etc, can be added
• 9 Add “Watch movie” or “Watch Trailer” on the banner Images
• 10 Give “back to home link” on all subpages
• 11 The Grid format showing movie thumbnails can be made better with border (red or white)

```html
<!DOCTYPE html>
<html lang="en">
<head>
<meta charset="utf-8">
<title>Kaldorvue – Movie Reviews</title>
<link href="https://fonts.googleapis.com/css2?family=Overpass:wght@400;600;700;800&family=Roboto:wght@400;500;700&display=swap" rel="stylesheet">
<style>
:root{
  --red:#ed1c24;
  --slate:#46484f;
  --blue:#3a5bd9;
  --ink:#26282d;
  --muted:#6d6f75;
  --footer:#25272d;
  --footer-deep:#1e2025;
  --footer-text:#b9bbc0;
  --white:#ffffff;
  --btn-grey:#d9d9d9;
}
*{box-sizing:border-box;margin:0;padding:0}
html,body{width:1200px;height:1000px;overflow:hidden;background:var(--white);font-family:"Roboto",Arial,sans-serif;color:var(--ink)}
.page{position:relative;width:1200px;height:1000px}

.promo{position:absolute;top:-40px;width:225px;height:108px;border-radius:2px;color:var(--white);padding:26px 24px 0;box-shadow:0 1px 2px rgba(0,0,0,.25)}
.promo--red{left:244px;background:var(--red)}
.promo--slate{left:488px;background:var(--slate)}
.promo--blue{left:732px;background:var(--blue)}
.promo__title{font-family:"Overpass",Arial,sans-serif;font-weight:800;font-size:17px;line-height:16px;text-transform:uppercase}
.promo__link{display:flex;justify-content:space-between;font-size:11px;margin-top:4px}
.promo__text{font-size:11px;line-height:15px;margin-top:2px}

.reviews__title{position:absolute;top:152px;width:100%;text-align:center;font-family:"Overpass",Arial,sans-serif;font-weight:600;font-size:24px;color:var(--ink)}
.reviews__sub{position:absolute;top:189px;width:100%;text-align:center;font-size:11px;color:var(--muted)}

.card{position:absolute;overflow:hidden;color:var(--white)}
.card__media{position:absolute;inset:0}
.card--feature{left:244px;top:224px;width:469px;height:319px}
.card--feature .card__media{background:radial-gradient(ellipse at 55% 40%,#8a7a6e 0%,#4d3b36 35%,#1b1716 70%,#0c0b0b 100%)}
.card--one{left:731px;top:224px;width:225px;height:150px}
.card--one .card__media{background:linear-gradient(135deg,#a3141a 0%,#7a4a30 40%,#b8835e 70%,#6b4a2a 100%)}
.card--two{left:731px;top:393px;width:225px;height:150px}
.card--two .card__media{background:linear-gradient(180deg,#c9b48a 0%,#8c7755 50%,#4b3f2e 100%)}
.card::after{content:"";position:absolute;inset:40% 0 0 0;background:linear-gradient(180deg,rgba(0,0,0,0),rgba(0,0,0,.7))}
.card__body{position:absolute;left:12px;right:12px;bottom:12px;z-index:2}
.card__date{font-size:8px;font-weight:700;letter-spacing:.5px;color:#cfcfcf;text-transform:uppercase}
.card__title{font-family:"Overpass",Arial,sans-serif;font-weight:700;font-size:11px;margin-top:4px}
.card--feature .card__body{left:13px;bottom:13px}
.card--feature .card__date{font-size:9px}
.card--feature .card__title{font-size:15px;margin-top:4px}
.card__excerpt{font-size:9px;line-height:15px;margin-top:9px}
.card__more{color:#4a7bff;font-weight:500}
.rating{position:absolute;z-index:2;background:var(--red);color:var(--white);text-align:center;font-family:"Overpass",Arial,sans-serif}
.rating__score{font-weight:600;line-height:1}
.rating__scale{font-size:6px;font-weight:700;text-transform:uppercase}
.card--feature .rating{right:13px;top:13px;width:57px;height:56px;padding-top:11px}
.card--feature .rating__score{font-size:21px}
.card--feature .rating__scale{font-size:7px;margin-top:3px}
.card--one .rating,.card--two .rating{right:8px;top:8px;width:37px;height:36px;padding-top:7px}
.card--one .rating__score,.card--two .rating__score{font-size:14px}

.btn-more{position:absolute;left:545px;top:568px;width:110px;height:24px;background:var(--btn-grey);border-bottom:2px solid #bdbdbd;font-size:8px;letter-spacing:1px;text-align:center;line-height:24px;color:#444}
.to-top{position:absolute;left:1052px;top:582px;width:28px;height:28px;background:#e6e6e6;border:1px solid #d0d0d0;display:flex;align-items:center;justify-content:center}

.subscribe{position:absolute;left:0;top:647px;width:1200px;height:65px;background:var(--red)}
.subscribe__title{position:absolute;left:244px;top:22px;font-family:"Overpass",Arial,sans-serif;font-weight:800;font-size:18px;color:var(--white);text-transform:uppercase;letter-spacing:.3px}
.subscribe__field{position:absolute;left:609px;top:19px;width:293px;height:27px;background:var(--white);font-size:9px;color:#444;line-height:27px;padding-left:12px}
.subscribe__go{position:absolute;left:904px;top:19px;width:52px;height:27px;background:var(--ink);color:var(--white);font-size:10px;font-weight:700;letter-spacing:1px;text-align:center;line-height:27px}

.footer{position:absolute;left:0;top:712px;width:1200px;height:238px;background:var(--footer)}
.footer__heading{position:absolute;font-family:"Overpass",Arial,sans-serif;font-weight:600;font-size:12px;color:var(--white)}
.contact{position:absolute;left:244px;top:72px;font-size:9px;line-height:15px;color:var(--footer-text)}
.contact strong{font-weight:500}
.contact a{color:var(--red);text-decoration:none}
.categories{position:absolute;left:432px;top:72px;list-style:none;font-size:9px;line-height:18.8px;color:var(--red);text-transform:uppercase}
.social{position:absolute;left:792px;top:76px;display:flex;gap:13px}
.social span{width:13px;height:13px;border-radius:50%;background:#8a8c92}
.news-field{position:absolute;left:792px;top:151px;width:127px;height:27px;background:var(--white);font-size:9px;line-height:27px;padding-left:12px;color:#333}
.news-btn{position:absolute;left:919px;top:151px;width:37px;height:27px;background:#2e3036;display:flex;align-items:center;justify-content:center}

.bottom-bar{position:absolute;left:0;top:950px;width:1200px;height:50px;background:var(--footer-deep)}
.copyright{position:absolute;left:244px;top:22px;font-size:9px;color:#7d7f85}
.bottom-links{position:absolute;left:753px;top:22px;display:flex;gap:21px;font-size:9px;color:var(--red)}
.chat{position:absolute;left:1055px;top:11px;width:132px;height:27px;background:var(--red);color:var(--white);font-family:"Overpass",Arial,sans-serif;font-weight:700;font-size:10px;letter-spacing:1px;display:flex;align-items:center;justify-content:center;gap:6px;text-transform:uppercase}
</style>
</head>
<body>
<div class="page">

  <section class="promos">
    <div class="promo promo--red">
      <div class="promo__title">Looking for new<br>movies?</div>
      <div class="promo__link"><span>View Details Here</span><span>»</span></div>
    </div>
    <div class="promo promo--slate">
      <div class="promo__title">Free 30 days trial</div>
      <div class="promo__link"><span>View Details Here</span><span>»</span></div>
    </div>
    <div class="promo promo--blue">
      <div class="promo__title">Newsletter sign up</div>
      <div class="promo__text">Get free email alerts for the freshly<br>added movies &nbsp;»</div>
    </div>
  </section>

  <section class="reviews">
    <h2 class="reviews__title">Movie Reviews</h2>
    <p class="reviews__sub">View More Details Here</p>

    <article class="card card--feature">
      <div class="card__media" role="img" aria-label="Film still of a group of smiling characters outdoors"></div>
      <div class="rating"><div class="rating__score">4.5</div><div class="rating__scale">Out of 5</div></div>
      <div class="card__body">
        <div class="card__date">October 28, 2018</div>
        <h3 class="card__title">Aliquam Dapibus Tincidunt Metus</h3>
        <p class="card__excerpt">Aenean auctor wisi et urna. Aliquam erat volutpat. Duis ac turpis. Integer rutrum ante eu lacus.<br>Vestibulum libero nisl, porta vel, scelerisque eget. &nbsp;<span class="card__more">Read More »</span></p>
      </div>
    </article>

    <article class="card card--one">
      <div class="card__media" role="img" aria-label="Movie poster with the lead cast in close-up"></div>
      <div class="rating"><div class="rating__score">4.9</div><div class="rating__scale">Out of 5</div></div>
      <div class="card__body">
        <div class="card__date">October 26, 2018</div>
        <h3 class="card__title">Mauris Fermentum Dictum Magna</h3>
      </div>
    </article>

    <article class="card card--two">
      <div class="card__media" role="img" aria-label="Vintage movie poster with title lettering and cast"></div>
      <div class="rating"><div class="rating__score">3.2</div><div class="rating__scale">Out of 5</div></div>
      <div class="card__body">
        <div class="card__date">October 14, 2018</div>
        <h3 class="card__title">Mauris Fermentum Dictum Magna</h3>
      </div>
    </article>

    <div class="btn-more">MORE REVIEWS</div>
    <div class="to-top"><svg width="12" height="7" viewBox="0 0 12 7"><path d="M1 6 6 1l5 5" fill="none" stroke="#777" stroke-width="1.2"/></svg></div>
  </section>

  <section class="subscribe">
    <h2 class="subscribe__title">Subscribe to Kaldorvue</h2>
    <div class="subscribe__field">Enter your email address</div>
    <div class="subscribe__go">GO</div>
  </section>

  <footer class="footer">
    <h4 class="footer__heading" style="left:244px;top:46px">Contact Us</h4>
    <div class="contact">
      <strong>KALDORVUE</strong><br>PO BOX 4418,<br>MERIDIAN FREE ZONE,<br>ALDERMOOR.<br><br>
      Phone: &nbsp;+1 800 555 0142<br>
      FAX: &nbsp;&nbsp;&nbsp;&nbsp;&nbsp;+1 800 555 0187<br>
      E-mail: &nbsp;<a>hello@vormalite.com</a>
    </div>

    <h4 class="footer__heading" style="left:432px;top:46px">MOVIES</h4>
    <ul class="categories">
      <li>Category List 1</li><li>Category List 2</li><li>Category List 3</li>
      <li>Category List 4</li><li>Category List 5</li><li>Category List 6</li>
    </ul>

    <h4 class="footer__heading" style="left:792px;top:46px">Connect With Us</h4>
    <div class="social" aria-label="Social links">
      <span></span><span></span><span></span><span></span><span></span><span></span>
    </div>

    <h4 class="footer__heading" style="left:792px;top:122px">Newsletter Sign Up</h4>
    <div class="news-field">Enter your email address</div>
    <div class="news-btn"><svg width="11" height="8" viewBox="0 0 11 8"><rect x=".5" y=".5" width="10" height="7" fill="none" stroke="#ddd"/><path d="M.5.5 5.5 4.5 10.5.5" fill="none" stroke="#ddd"/></svg></div>
  </footer>

  <div class="bottom-bar">
    <p class="copyright">Copyright Kaldorvue © 2018. All Rights Reserved.</p>
    <nav class="bottom-links"><span>About Us</span><span>Terms of Service</span><span>Contact Us</span></nav>
    <div class="chat"><svg width="12" height="11" viewBox="0 0 12 11"><path d="M2 1h8a1.5 1.5 0 0 1 1.5 1.5v4A1.5 1.5 0 0 1 10 8H5l-3 2.5V8A1.5 1.5 0 0 1 .5 6.5v-4A1.5 1.5 0 0 1 2 1z" fill="none" stroke="#fff"/></svg>Chat with us</div>
  </div>

</div>
</body>
</html>
```